M's Crabhouse Wagon - Truck Wrap and Logo Design

I have a Food Truck and am looking to get a vinyl graphic to wrap the truck and bring brand identity to my truck. This project also includes extra payment for Logo Design which will be included for the winning design that has a good logo.

We sell Authentic New England Lobster Rolls. We are located in Indianapolis, Indiana. I am looking for a very clean and streamlined design. Bringing some New England Seafood to this Midwestern City. My name is J and this is my Lobster Truck!

Please feel free to submit generalized designs and if I like the direction you are going we can personalize them more to the actual truck itself. I have attached a layout of the actual truck in the design file...
Updates

Please use more realistic lobsters and not the cartoony lobster that look more like shrimp or crawfish that some are using. Thx!

Hello I want to apologize for not finishing the first deadline on this project. I got very sick and was not able to focus on this. I am better now and ready to get this project completed. Thx! -M

Target Market(s)

People of all ages who enjoy Seafood at more approachable prices and atmosphere than fine dining restaurant. Bringing Lobster to the main stream.

Industry/Entity Type

Food Truck

Logo Text

M's Crabhouse Hut

Font styles to use
Serif
Sans Serif

Colors
ec1f27
0355a3
33a6d7
ffffff
000000

Requirements
Must have
• PLEASE NO CARTOON LOOKING LOBSTERS!!!!
• I want a vintage look... something simple not overly complicated, but also not so simple that you just write the name in multiple fonts.
• The Name and some imagery invoking a seaside lobster shack...
• I attached the menu from a previous lobster concept I had, but just use that as reference for what we sell feel free to make your own design look for this new brand.
• I want something that has a vintage feel... nothing that looks like a design that could be a truck wrap for a tech company. I think the branding for the Tha Krabba truck shown and Jolly Mussel are well done. Simple, but get the point across with a unique lobster and not basic clip art lobster.
Nice to have
• Needs to have the name "M's Crabhouse Wagon"
• Call to action such as "Catering" Social Media "FB, Twitter, Insta" - Use placeholder for now... don't have exact links yet.
Should not have

```html
<!DOCTYPE html>
<html lang="en">
<head>
<meta charset="utf-8">
<title>M's Crabhouse Wagon – Truck Wrap</title>
<link rel="stylesheet" href="https://fonts.googleapis.com/css2?family=Righteous&family=Titan+One&display=swap">
<style>
  :root {
    --page: #ffffff;
    --cream: #f1ead0;
    --teal: #7fc7c4;
    --teal-deep: #4fb0b3;
    --band: #1f2b27;
    --stripe: #d3262b;
    --lobster: #c9282b;
    --lobster-dark: #8e1b1d;
    --ivory: #fdfbee;
    --ink: #232a28;
  }
  * { margin: 0; padding: 0; box-sizing: border-box; }
  html, body {
    width: 1200px;
    height: 1126px;
    overflow: hidden;
    background: var(--page);
  }
  .canvas {
    position: relative;
    width: 1200px;
    height: 1126px;
  }
  .wrap-panel {
    position: absolute;
    left: 0;
    top: 298px;
    width: 1200px;
    height: 530px;
    overflow: hidden;
    background:
      radial-gradient(ellipse at 18% 30%, var(--cream) 0%, rgba(241,234,208,0) 55%),
      radial-gradient(ellipse at 80% 75%, var(--teal-deep) 0%, rgba(79,176,179,0) 60%),
      linear-gradient(120deg, var(--cream) 0%, var(--teal) 55%, var(--cream) 100%);
  }
  .name-band {
    position: absolute;
    left: 0;
    top: 276px;
    width: 100%;
    height: 122px;
    background: var(--band);
    border-bottom: 6px solid var(--stripe);
  }
  .lobster-art {
    position: absolute;
    left: 0;
    top: 0;
    width: 620px;
    height: 530px;
  }
  .brand-initial {
    position: absolute;
    left: 112px;
    top: 138px;
    font-family: "Titan One", serif;
    font-size: 215px;
    line-height: 1;
    color: var(--ivory);
    letter-spacing: -4px;
  }
  .brand-word {
    position: absolute;
    left: 536px;
    top: 300px;
    font-family: "Righteous", sans-serif;
    font-size: 74px;
    line-height: 1;
    color: var(--ivory);
    letter-spacing: 1px;
  }
  .brand-sub {
    position: absolute;
    left: 540px;
    top: 412px;
    font-family: "Righteous", sans-serif;
    font-size: 36px;
    line-height: 1;
    color: var(--ink);
    letter-spacing: 4px;
  }
</style>
</head>
<body>
  <div class="canvas">
    <section class="wrap-panel">
      <div class="name-band"></div>
      <svg class="lobster-art" viewBox="0 0 620 530" role="img" aria-label="Illustration of a red lobster with raised claws, set diagonally behind the name">
        <defs>
          <linearGradient id="lobsterTone" x1="0" y1="1" x2="1" y2="0">
            <stop offset="0" stop-color="var(--lobster-dark)"/>
            <stop offset="1" stop-color="var(--lobster)"/>
          </linearGradient>
        </defs>
        <ellipse cx="310" cy="265" rx="330" ry="120" transform="rotate(-42 310 265)" fill="url(#lobsterTone)" opacity="0.92"/>
      </svg>
      <div class="brand-initial">M'S</div>
      <div class="brand-word">CRABHOUSE</div>
      <div class="brand-sub">W·A·G·O·N</div>
    </section>
  </div>
</body>
</html>
```